Business Card Design Project

I'm moving my dental office and would like to use my existing logo to create a new:
- Business Card (submit here)
- Appointment Card (please submit to this project - http://tasks.briefhub.example/task.aspx?id=463519)
- Letterhead (please submit to this project - http://tasks.briefhub.example/task.aspx?id=463519)
- Envelope (please submit to this project - http://tasks.briefhub.example/task.aspx?id=463519)

My practice name (within my logo) is:
Morris T. Vale, D.D.S., P.A.
Family and Cosmetic Dentistry

***Obviously you will notice that the lower leg of the "K" in my logo is a smile.

My new address and contact information is:
350 Linden Meadow Drive, Suite 118
Cary, NC 27603

919-472-3180 (ph)
919-472-3195 (fax)
www.valedds.example

If you would like to use a tagline, I would suggest "Precision Dentistry with a Personal Touch".

I have attached my logo in numerous formats - please download attached logos here - http://tasks.briefhub.example/task.aspx?id=463519

I have also attached 2 QR codes, one of which links to my website and the other one which links to a "Like" page for my business Chatterly page. These QR codes could be improved by putting a graphic in the middle, but I created these myself and did not know how to do this.

Thank you for your time. I look forward to seeing all of your creative ideas!

Depending on the designs, I may award 2 different winners for the Business Card project and the Stationery Project. Or if a design is really good, I will award both projects to the same designer.

Reason: Initially I had bundled my entire project (stationary, envelope, business card, etc.) into one contest but BriefHub has recommended that I split it into two distinct projects (business card AND stationary, envelope, etc.). Therefore I'm extending the deadline so that I receive enough designs. Thank you.

Target Market(s)

Current and prospective dental patients.

Industry/Entity Type

Dental

Requirements
Must have
• Please ensure business card has a 2-sided design.
Please ensure that your design is "practical" for printing purposes.
Nice to have
• Improvement of QR codes by addition of graphics in the middle to differentiate them. Incorporation of QR codes into business card design, maybe on the back side?

```html
<!DOCTYPE html>
<html lang="en">
<head>
<meta charset="utf-8">
<title>Morris T. Vale, D.D.S., P.A. – Business Card</title>
<link rel="stylesheet" href="https://fonts.googleapis.com/css2?family=Crimson+Pro:wght@400;600&display=swap">
<style>
  :root {
    --page: #ffffff;
    --card: #f2f3f3;
    --rim: #fbfbfb;
    --navy: #1b1d5c;
    --blue: #2743a0;
    --teal: #0f6a68;
    --grey: #9a9c9e;
  }
  * { box-sizing: border-box; margin: 0; padding: 0; }
  html, body { width: 1200px; height: 900px; overflow: hidden; background: var(--page); }
  body { font-family: "Crimson Pro", Georgia, serif; position: relative; }

  .card {
    position: absolute; top: 310px; width: 500px; height: 280px;
    background: var(--card); border-radius: 24px;
    box-shadow: 0 0 0 6px var(--rim), 0 6px 14px rgba(0,0,0,.18);
  }
  .card--front { left: 70px; }
  .card--back { left: 630px; }
  .card__frame {
    position: absolute; inset: 14px; border-radius: 16px;
    border: 2.5px solid var(--blue);
    border-right-color: var(--teal); border-bottom-color: var(--teal);
  }

  .brand { display: flex; align-items: center; gap: 10px; }
  .brand__square { width: 50px; height: 50px; background: var(--teal); flex: none; }
  .brand__name {
    font-weight: 600; color: var(--navy); font-variant: small-caps;
    font-size: 23px; line-height: 1; letter-spacing: .2px;
    border-bottom: 1px solid var(--navy); padding-bottom: 2px;
  }
  .brand__field {
    font-weight: 600; color: var(--teal); font-variant: small-caps;
    font-size: 14px; letter-spacing: 1px; margin-top: 2px; text-align: center;
  }
  .card--front .brand { position: absolute; left: 92px; top: 112px; }

  .details { position: absolute; left: 50px; top: 36px; color: var(--teal); font-size: 16px; line-height: 21px; }
  .details__name { font-size: 20px; font-weight: 600; color: var(--navy); line-height: 24px; }
  .details__field { color: var(--navy); font-size: 17px; }
  .contacts { list-style: none; margin-top: 18px; }
  .contacts li { display: flex; align-items: center; gap: 12px; height: 30px; font-size: 16px; }
  .contacts svg { width: 18px; height: 18px; }

  .back-mark { position: absolute; right: 32px; top: 94px; width: 140px; text-align: center; }
  .back-mark .brand__square { width: 56px; height: 56px; margin: 0 auto 8px; }
  .back-mark__name { font-weight: 600; color: var(--navy); font-variant: small-caps; font-size: 11.5px; border-bottom: 1px solid var(--navy); }
  .back-mark__field { font-weight: 600; color: var(--teal); font-variant: small-caps; font-size: 8px; letter-spacing: .4px; }
  .back-mark__tagline { color: var(--grey); font-size: 11.5px; line-height: 15px; margin-top: 18px; }
</style>
</head>
<body>
  <section class="card card--front" aria-label="Business card front">
    <div class="card__frame"></div>
    <div class="brand">
      <span class="brand__square"></span>
      <div>
        <div class="brand__name">Morris T. Vale, D.D.S., P.A.</div>
        <div class="brand__field">Family and Cosmetic Dentistry</div>
      </div>
    </div>
  </section>

  <section class="card card--back" aria-label="Business card back">
    <div class="card__frame"></div>
    <div class="details">
      <div class="details__name">Morris T. Vale, D.D.S., P.A.</div>
      <div class="details__field">Family and Cosmetic Dentistry</div>
      <div>350 Linden Meadow Drive, Suite 118</div>
      <div>Cary, NC 27603</div>
      <ul class="contacts">
        <li>
          <svg viewBox="0 0 20 20" aria-label="Phone"><path fill="var(--teal)" d="M2 8c0-3 4-4 8-4s8 1 8 4v1h-4V7H6v2H2zM5 10h10l2 6H3z"/></svg>
          919-472-3180
        </li>
        <li>
          <svg viewBox="0 0 20 20" aria-label="Fax"><rect x="3" y="2" width="14" height="16" rx="1.5" fill="var(--teal)"/><path d="M6 7h8M6 10h8M6 13h8" stroke="#f2f3f3" stroke-width="1.2"/></svg>
          919-472-3195
        </li>
        <li>
          <svg viewBox="0 0 20 20" aria-label="Website"><circle cx="10" cy="10" r="8" fill="var(--teal)"/><g fill="none" stroke="#f2f3f3" stroke-width="1"><ellipse cx="10" cy="10" rx="3.5" ry="8"/><path d="M2 10h16M4 5.5h12M4 14.5h12M10 2v16"/></g></svg>
          www.valedds.example
        </li>
      </ul>
    </div>
    <div class="back-mark">
      <div class="brand__square"></div>
      <div class="back-mark__name">Morris T. Vale, D.D.S., P.A.</div>
      <div class="back-mark__field">Family and Cosmetic Dentistry</div>
      <p class="back-mark__tagline">Precision Dentistry<br>with a Personal Touch</p>
    </div>
  </section>
</body>
</html>
```